ARC VOLLEY Business Card Project

I'd like to request a business card design for the new company I've launched.
The name of the company is "ARC VOLLEY" an indoor unmanned tennis practice facility.
We would like to see designs that use our brand identity color in the logo I've attached.
We hope to get the design with modern, luxurious and elegant tone and manner.
We hope the logo should not be too big.

Business card must have elements as below:
- Logo (One of the logos I've attached)
- Name (In Korean Text) : 박 서 윤
- Title (In Korean Text) : 대표
- Phone Number : 010-8472-3916
- Email Address : seoyun.park@arcvolley-example.co.kr
- Website : www.arcvolley-example.co.kr
- Instagram : arcvolley
- Address (In Korean text) : 경기도 용인시 수지구 풍덕천로 456 미래타워 5층 501호, 502호

Target Market(s)

Tennis amateurs in 20 to 40s

Industry/Entity Type

Sports, Hobby

Contact Information for Business Card

- Logo (One of the logos I've attached) - Name (In Korean Text) : 박 서 윤 - Title (In Korean Text) : 대표 - Phone Number : 010-8472-3916 - Email Address : seoyun.park@arcvolley-example.co.kr - Website : www.arcvolley-example.co.kr - Instagram : arcvolley - Address (In Korean text) : 경기도 용인시 수지구 풍덕천로 456 미래타워 5층 501호, 502호

Font styles to use
Sans Serif

Requirements
Must have
• Double sided
Nice to have
• Logo with intaglio or relief embossing
Should not have
• Logo should not be too big.

```html
<!DOCTYPE html>
<html lang="ko">
<head>
<meta charset="utf-8">
<title>ARC VOLLEY Business Card</title>
<link href="https://fonts.googleapis.com/css2?family=Noto+Serif+KR:wght@400;600;700&display=swap" rel="stylesheet">
<style>
  :root {
    --backdrop: #2a2a2a;
    --green-card: #2c5338;
    --green-deep: #1f4a2c;
    --green-soft: #4a7a58;
    --paper: #f1f1ef;
    --ink: #3a3a3a;
    --name-light: #dcdcd8;
  }
  * { margin: 0; padding: 0; box-sizing: border-box; }
  html, body { width: 1200px; height: 1138px; overflow: hidden; }
  body {
    background: var(--backdrop);
    font-family: "Noto Serif KR", serif;
    position: relative;
  }
  .card {
    position: absolute;
    width: 620px;
    height: 376px;
    border-radius: 16px;
    overflow: hidden;
  }
  .card--front { left: 274px; top: 186px; background: var(--green-card); }
  .card--back { left: 276px; top: 608px; background: var(--paper); }

  .front-mark {
    position: absolute;
    left: 272px; top: 104px;
    width: 76px; height: 76px;
    border-radius: 50%;
    background: var(--green-soft);
  }
  .front-name {
    position: absolute;
    left: 0; right: 0; top: 228px;
    text-align: center;
    font-size: 38px;
    font-weight: 600;
    letter-spacing: 1px;
    color: var(--name-light);
  }

  .back-mark {
    position: absolute;
    left: 52px; top: 188px;
    width: 152px; height: 152px;
    border-radius: 50%;
    background: var(--green-deep);
  }
  .back-brand {
    position: absolute;
    right: 30px; top: 28px;
    font-size: 32px;
    font-weight: 600;
    letter-spacing: 1px;
    color: var(--green-deep);
  }
  .person {
    position: absolute;
    right: 30px; top: 110px;
    text-align: right;
  }
  .person__name {
    font-size: 28px;
    font-weight: 700;
    letter-spacing: 2px;
    color: var(--green-deep);
    line-height: 1.2;
  }
  .person__title {
    font-size: 13px;
    font-weight: 600;
    color: var(--ink);
    margin-top: 2px;
  }
  .contacts {
    position: absolute;
    right: 26px; top: 222px;
    list-style: none;
    text-align: right;
    font-size: 14px;
    color: var(--ink);
  }
  .contacts li {
    height: 23.5px;
    display: flex;
    justify-content: flex-end;
    align-items: center;
    gap: 6px;
  }
  .contacts svg { width: 12px; height: 12px; fill: var(--green-deep); flex: none; }
  .contacts .spacer { width: 12px; flex: none; }
  .social-dot {
    width: 11px; height: 11px;
    border: 1.6px solid var(--green-deep);
    border-radius: 50%;
    margin-right: 8px;
    flex: none;
  }
</style>
</head>
<body>
  <section class="card card--front">
    <div class="front-mark"></div>
    <div class="front-name">ARC VOLLEY</div>
  </section>

  <section class="card card--back">
    <div class="back-mark"></div>
    <div class="back-brand">ARC VOLLEY</div>
    <div class="person">
      <div class="person__name">박 서 윤</div>
      <div class="person__title">대표</div>
    </div>
    <ul class="contacts">
      <li>010-8472-3916
        <svg viewBox="0 0 12 12"><path d="M1 4c0-2 2-3 5-3s5 1 5 3v1H8.5V3.8h-5V5H1zM3 6h6l1.5 5h-9z"/></svg>
      </li>
      <li>seoyun.park@arcvolley-example.co.kr
        <svg viewBox="0 0 12 12"><path d="M0 2h12v8H0zM1 3l5 4 5-4v-0.2H1z" fill-rule="evenodd"/></svg>
      </li>
      <li>#arcvolley <span class="social-dot"></span>www.arcvolley-example.co.kr
        <svg viewBox="0 0 12 12"><circle cx="6" cy="6" r="5.3" fill="none" stroke="currentColor" stroke-width="1.2" style="stroke:var(--green-deep)"/><path d="M0.7 6h10.6M6 0.7v10.6M6 0.7c-3 3-3 7.6 0 10.6M6 0.7c3 3 3 7.6 0 10.6" fill="none" stroke-width="1" style="stroke:var(--green-deep)"/></svg>
      </li>
      <li>경기도 용인시 수지구 풍덕천로
        <svg viewBox="0 0 12 12"><path d="M6 0.5a4 4 0 0 1 4 4c0 3-4 7-4 7s-4-4-4-7a4 4 0 0 1 4-4zm0 2.2a1.8 1.8 0 1 0 0 3.6 1.8 1.8 0 0 0 0-3.6z" fill-rule="evenodd"/></svg>
      </li>
      <li>456 미래타워 5층 501호, 502호<span class="spacer"></span></li>
    </ul>
  </section>
</body>
</html>
```